Webdesign für Fahrschule
Petra Lindqvor
Sehr ansprechendes, modernes und übersichtliches Design, welches das Unternehmen sehr gut widerspiegelt
Zielgruppe
Fahrschule mit fach- und sachgerechter Fahrschulausbildung in allen Zweiradklassen und im PKW-Bereich sowie Ausbildung auf Automatikfahrzeugen und Führerscheinausbildung für Behinderte
Aufgabenstellung
Keine Kopie der alten Seite
Nutzerfreundliche Unternehmenswebseite
Design soll frisch, modern und aussagekräftig erscheinen

```html
<!DOCTYPE html>
<html lang="en">
<head>
<meta charset="utf-8">
<title>Tolesk Drive – Driving Made Easy</title>
<link rel="stylesheet" href="https://fonts.googleapis.com/css2?family=Space+Grotesk:wght@400;500;600&family=Outfit:wght@300;400;500;600&display=swap">
<style>
:root{
  --lime:#b8d52e;
  --lime-soft:#c6dd4a;
  --lime-deep:#8fa820;
  --ink:#141414;
  --ink-soft:#3a3a3a;
  --field:#efefef;
  --white:#ffffff;
  --head:"Space Grotesk",sans-serif;
  --body:"Outfit",sans-serif;
}
*{box-sizing:border-box;margin:0;padding:0}
html,body{width:1200px;height:4474px;overflow:hidden}
body{position:relative;background:var(--white);color:var(--ink);font-family:var(--body)}
.abs{position:absolute}
.head{font-family:var(--head);font-weight:400;color:var(--ink)}

/* header */
.site-header{position:absolute;left:0;top:0;width:1200px;height:73px;background:rgba(255,255,255,.72);z-index:5}
.brand{position:absolute;left:61px;top:22px;font-family:var(--body);font-weight:600;font-size:20px;color:var(--ink);display:flex;align-items:center;gap:10px}
.brand-dot{width:14px;height:14px;border-radius:50%;background:var(--lime)}
.main-nav{position:absolute;right:60px;top:28px;display:flex;gap:20px;font-size:13.5px}
.main-nav span{color:var(--ink)}

/* hero */
.hero{position:absolute;left:0;top:0;width:1200px;height:727px;overflow:hidden;
  background:linear-gradient(100deg,#1e2b5a 0%,#2c3f7a 30%,#6b7590 55%,#a9a39a 75%,#8a8d92 100%)}
.hero-photo{position:absolute;inset:0;background:
  radial-gradient(ellipse 380px 260px at 120px 110px,rgba(200,40,50,.55),transparent 70%),
  radial-gradient(ellipse 420px 420px at 720px 380px,rgba(70,90,140,.5),transparent 70%),
  linear-gradient(180deg,rgba(0,0,0,0) 50%,rgba(10,20,40,.45) 100%)}
.hero-title{position:absolute;left:61px;top:148px;font-family:var(--head);font-weight:500;color:var(--white);font-size:80px;line-height:76px;letter-spacing:1px}
.hero-title small{display:block;font-size:70px;letter-spacing:0}
.hero-text{position:absolute;left:61px;top:325px;width:360px;color:var(--white);font-size:13px;line-height:22px}
.btn{position:absolute;display:flex;align-items:center;justify-content:center;border-radius:30px;font-size:16px;color:var(--ink);background:var(--lime);box-shadow:0 0 0 3px rgba(184,213,46,.35)}
.hero-btn{left:61px;top:457px;width:248px;height:47px}
.orbit{position:absolute;border-radius:50%;display:flex;flex-direction:column;align-items:center;justify-content:center;font-size:25px;gap:6px}
.orbit-ring{position:absolute;border-radius:50%;border:2px dashed rgba(255,255,255,.8)}
.orbit-train{left:807px;top:559px;width:140px;height:140px;background:var(--lime);color:var(--ink)}
.orbit-lic{left:991px;top:559px;width:140px;height:140px;background:rgba(40,40,45,.55);color:var(--white)}

/* registration */
.label{position:absolute;font-size:21px;color:var(--ink)}
.h2{position:absolute;font-family:var(--head);font-size:43px;line-height:44px;color:var(--ink)}
.reg-photo{position:absolute;left:61px;top:969px;width:504px;height:528px;border-radius:22px;
  background:linear-gradient(135deg,#8fb0c8 0%,#dfe6ea 35%,#c99a6e 55%,#e7eef2 75%,#6fb8d8 100%)}
.reg-corner{position:absolute;left:35px;top:1355px;width:160px;height:168px;border-left:13px solid var(--lime);border-bottom:13px solid var(--lime);border-bottom-left-radius:22px}
.h3{position:absolute;font-size:22px;font-weight:500;color:var(--ink)}
.lead{position:absolute;font-size:12.5px;line-height:22px;color:var(--ink-soft)}
.step{position:absolute;left:601px;width:540px;display:flex}
.step-name{position:relative;width:196px;padding-left:22px;font-size:17.5px;font-weight:500;line-height:21px}
.step-name::before{content:"";position:absolute;left:0;top:13px;width:9px;height:9px;border-radius:50%;background:var(--lime)}
.step-desc{flex:1;font-size:12.5px;line-height:21px;color:var(--ink-soft)}
.why{position:absolute;left:601px;display:flex;align-items:center;gap:14px;font-size:12.5px;color:var(--ink-soft)}
.why b{font-weight:600;color:var(--ink)}
.tick{width:24px;height:24px;border-radius:50%;background:var(--lime);display:flex;align-items:center;justify-content:center}
.reg-btn{left:601px;top:1473px;width:170px;height:52px}

/* seminar */
.seminar{position:absolute;left:0;top:1612px;width:1200px;height:868px;background:var(--lime);overflow:hidden}
.seminar-bg{position:absolute;inset:0;background:
  radial-gradient(ellipse 520px 260px at 380px 470px,rgba(255,255,255,.18),transparent 70%),
  radial-gradient(ellipse 200px 300px at 850px 120px,rgba(255,255,255,.16),transparent 70%)}
.sem-btn{left:966px;top:99px;width:174px;height:47px;background:var(--white);box-shadow:none;font-size:17px}
.feature{position:absolute;z-index:3;display:flex;align-items:center;gap:28px;font-size:22px;line-height:31px;color:var(--ink)}
.f-icon{width:64px;height:64px;border-radius:50%;background:rgba(255,255,255,.28);display:flex;align-items:center;justify-content:center;flex:none}
.f-icon.on{background:var(--white)}
.sem-photo{position:absolute;z-index:1;left:660px;top:220px;width:480px;height:457px;border-radius:10px;
  background:linear-gradient(180deg,#9fb6d0 0%,#d5dde4 32%,#6f6f72 45%,#4d4d50 100%)}
.sem-block{position:absolute;z-index:2;left:660px;top:257px;width:114px;height:384px;background:var(--lime);border-radius:0 8px 8px 0;opacity:.9}
.sem-bracket{position:absolute;left:1040px;top:552px;width:122px;height:147px;border-right:12px solid var(--white);border-bottom:12px solid var(--white);border-bottom-right-radius:14px}
.sem-text{position:absolute;left:61px;top:718px;width:1070px;font-size:13px;line-height:22px;color:var(--ink)}
.info{position:absolute;width:300px;text-align:center}
.info-icon{width:94px;height:94px;border-radius:50%;background:var(--white);margin:0 auto 12px;display:flex;align-items:center;justify-content:center;box-shadow:0 2px 8px rgba(0,0,0,.08)}
.info h4{font-family:var(--head);font-weight:400;font-size:29px;line-height:36px}
.info p{font-size:19px}

/* data protection */
.center{position:absolute;left:0;width:1200px;text-align:center}
.ring{position:absolute;left:410px;top:2887px;width:382px;height:382px;border-radius:50%;border:5px solid var(--lime)}
.globe{position:absolute;left:476px;top:2953px;width:250px;height:250px;border-radius:50%;
  background:radial-gradient(circle at 40% 35%,#b8d52e 0%,#8fa820 45%,#5f7214 100%)}
.node{position:absolute;width:72px;height:72px;border-radius:50%;background:var(--white);box-shadow:0 2px 10px rgba(0,0,0,.1);display:flex;align-items:center;justify-content:center}
.dp{position:absolute;font-size:12.5px;line-height:21px;color:var(--ink-soft)}
.dp strong{display:block;font-size:17px;font-weight:500;color:var(--ink);line-height:22px}

/* contact */
.contact-band{position:absolute;left:0;top:3262px;width:1200px;height:338px;background:var(--lime)}
.field{position:absolute;background:var(--field);border-radius:14px;font-size:13px;color:var(--ink-soft);padding:17px 18px}
.submit{left:472px;top:3868px;width:256px;height:49px}

/* footer */
.site-footer{position:absolute;left:0;top:3992px;width:1200px;height:482px;background:linear-gradient(180deg,#c3db3a 0%,#b8d52e 60%,#aac82a 100%)}
.foot-brand{position:absolute;left:0;width:1200px;top:150px;text-align:center;font-weight:600;font-size:38px;color:var(--ink)}
.foot-nav{position:absolute;left:0;width:1200px;top:252px;display:flex;justify-content:center;gap:20px;font-size:13.5px}
.social{position:absolute;left:0;width:1200px;top:311px;display:flex;justify-content:center;gap:22px}
.social span{width:30px;height:30px;border-radius:50%;background:var(--white)}
.foot-rule{position:absolute;left:61px;top:413px;width:1080px;height:1px;background:var(--ink)}
.foot-copy{position:absolute;left:61px;top:432px;font-size:11px}
.foot-links{position:absolute;right:60px;top:432px;display:flex;gap:30px;font-size:11px}
</style>
</head>
<body>

<header class="site-header">
  <div class="brand"><span class="brand-dot"></span>Tolesk Drive</div>
  <nav class="main-nav"><span>Home</span><span>Registration</span><span>Advanced Seminar</span><span>Data Protection</span><span>Imprint</span><span>Contact</span></nav>
</header>

<section class="hero">
  <div class="hero-photo" role="img" aria-label="Photo of a smiling man in a wheelchair getting into a car"></div>
  <h1 class="hero-title">DRIVING<small>Made Easy</small></h1>
  <p class="hero-text">We're Committed To Providing Professional, High-Quality Driving Lessons For Everyone—Whether You're A First-Time Driver, Looking To Switch To An Automatic Vehicle, Or Seeking Advanced Driving Seminars.</p>
  <div class="btn hero-btn">Book Your Lesson Now</div>
  <div class="orbit-ring" style="left:797px;top:549px;width:160px;height:160px"></div>
  <div class="orbit-ring" style="left:981px;top:549px;width:160px;height:160px"></div>
  <div class="orbit orbit-train">
    <svg width="22" height="22" viewBox="0 0 22 22"><path d="M5 17L17 5M8 5h9v9" fill="none" stroke="#141414" stroke-width="2"/></svg>Traning</div>
  <div class="orbit orbit-lic">
    <svg width="22" height="22" viewBox="0 0 22 22"><path d="M5 17L17 5M8 5h9v9" fill="none" stroke="#fff" stroke-width="2"/></svg>License</div>
</section>

<section class="registration">
  <div class="label" style="left:61px;top:796px">Registration</div>
  <h2 class="h2" style="left:61px;top:829px">Take The First Step, Register<br>Today</h2>
  <div class="reg-corner"></div>
  <div class="reg-photo" role="img" aria-label="Photo of a woman in a car holding up her new driving licence"></div>
  <h3 class="h3" style="left:601px;top:928px">How To Register</h3>
  <p class="lead" style="left:601px;top:974px;width:540px">Ready To Get Behind The Wheel? It's Easy To Start Your Journey With Whether You're A Beginner, Looking To Switch To An Automatic Car, Or Want Specialized Training, We've Got You Covered.</p>
  <div class="step" style="top:1064px"><div class="step-name">Choose Your License Class</div><div class="step-desc">Select The Driving Class That Best Suits Your Needs—Whether It's For A Car, Motorcycle, Or Automatic Vehicle</div></div>
  <div class="step" style="top:1149px"><div class="step-name">Fill Out The Registration Form</div><div class="step-desc">Simply Provide Your Details Below To Reserve Your Spot In One Of Our Classes.</div></div>
  <div class="step" style="top:1213px"><div class="step-name">Book Your First Lesson</div><div class="step-desc">Select The Driving Class That Best Suits Your Needs—Whether It's For A Car, Motorcycle, Or Automatic Vehicle</div></div>
  <h3 class="h3" style="left:601px;top:1299px">Why Register With Us?</h3>
  <div class="why" style="top:1345px"><span class="tick"><svg width="12" height="10" viewBox="0 0 12 10"><path d="M1 5l3.5 3.5L11 1" fill="none" stroke="#141414" stroke-width="1.6"/></svg></span><span><b>Expert Instructors:</b> Learn From Certified, Experienced Professionals.</span></div>
  <div class="why" style="top:1382px"><span class="tick"><svg width="12" height="10" viewBox="0 0 12 10"><path d="M1 5l3.5 3.5L11 1" fill="none" stroke="#141414" stroke-width="1.6"/></svg></span><span><b>Flexible Schedule:</b> Choose Lessons That Fit Your Availability</span></div>
  <div class="why" style="top:1420px"><span class="tick"><svg width="12" height="10" viewBox="0 0 12 10"><path d="M1 5l3.5 3.5L11 1" fill="none" stroke="#141414" stroke-width="1.6"/></svg></span><span><b>Safe Learning Environment:</b> Focused On Teaching Safe And Responsible Driving</span></div>
  <div class="btn reg-btn">Register Now</div>
</section>

<section class="seminar">
  <div class="seminar-bg" role="img" aria-label="Faded photo of a driving instructor beside a car"></div>
  <div class="label" style="left:61px;top:56px">Advanced Seminar</div>
  <h2 class="h2" style="left:61px;top:90px">Unlock Advanced Driving<br>Skills For Any Situation</h2>
  <div class="btn sem-btn">Register Now</div>

  <div class="sem-bracket"></div>
  <div class="sem-photo" role="img" aria-label="Photo of a white car driving through orange traffic cones on a training ground"></div>
  <div class="sem-block"></div>

  <div class="feature" style="left:61px;top:293px"><span class="f-icon on"><svg width="30" height="30" viewBox="0 0 30 30"><circle cx="15" cy="15" r="12" fill="none" stroke="#141414" stroke-width="2"/><path d="M9 15l4.5 4.5L25 8" fill="none" stroke="#141414" stroke-width="2"/></svg></span><span>Defensive Driving<br>Techniques</span></div>
  <div class="feature" style="left:432px;top:293px"><span class="f-icon"><svg width="30" height="30" viewBox="0 0 30 30"><circle cx="15" cy="15" r="12" fill="none" stroke="#fff" stroke-width="2"/><path d="M9 15l4.5 4.5L25 8" fill="none" stroke="#fff" stroke-width="2"/></svg></span><span>Mastering Complex<br>Road Conditions</span></div>
  <div class="feature" style="left:61px;top:417px"><span class="f-icon"><svg width="30" height="30" viewBox="0 0 30 30"><circle cx="15" cy="15" r="12" fill="none" stroke="#fff" stroke-width="2"/><path d="M9 15l4.5 4.5L25 8" fill="none" stroke="#fff" stroke-width="2"/></svg></span><span>Advanced Vehicle<br>Contro</span></div>
  <div class="feature" style="left:432px;top:417px"><span class="f-icon"><svg width="30" height="30" viewBox="0 0 30 30"><circle cx="15" cy="15" r="12" fill="none" stroke="#fff" stroke-width="2"/><path d="M9 15l4.5 4.5L25 8" fill="none" stroke="#fff" stroke-width="2"/></svg></span><span>Eco-Friendly<br>Driving:</span></div>
  <div class="feature" style="left:61px;top:540px"><span class="f-icon"><svg width="30" height="30" viewBox="0 0 30 30"><circle cx="15" cy="15" r="12" fill="none" stroke="#fff" stroke-width="2"/><path d="M9 15l4.5 4.5L25 8" fill="none" stroke="#fff" stroke-width="2"/></svg></span><span>Enhanced Road<br>Safety Awareness</span></div>
  <div class="feature" style="left:432px;top:540px"><span class="f-icon"><svg width="30" height="30" viewBox="0 0 30 30"><circle cx="15" cy="15" r="12" fill="none" stroke="#fff" stroke-width="2"/><path d="M9 15l4.5 4.5L25 8" fill="none" stroke="#fff" stroke-width="2"/></svg></span><span>Improved Night<br>Driving Skills:</span></div>

  <p class="sem-text">Join Us For An In-Depth, Hands-On Learning Experience In Our Defensive Driving Techniques Seminar. This Seminar Is Designed For Drivers Who Want To Enhance Their Safety And Preparedness Behind The Wheel. Whether You're A New Driver Or An Experienced One, Our Expert Instructors Will Guide You Through Defensive Driving Techniques That Can Save Lives.</p>
</section>

<div class="info" style="left:84px;top:2428px">
  <div class="info-icon"><svg width="44" height="44" viewBox="0 0 44 44" fill="none" stroke="#141414" stroke-width="1.8"><path d="M10 5h22M10 39h22M12 5c0 10 9 12 9 17s-9 7-9 17M30 5c0 10-9 12-9 17s9 7 9 17"/><circle cx="34" cy="30" r="7"/><path d="M34 26v4l2 2"/></svg></div>
  <h4>Duration</h4><p>X Hours/Days</p>
</div>
<div class="info" style="left:451px;top:2428px">
  <div class="info-icon"><svg width="44" height="44" viewBox="0 0 44 44" fill="none" stroke="#141414" stroke-width="1.8"><path d="M22 34s-11-11-11-19a11 11 0 0 1 22 0c0 8-11 19-11 19z"/><circle cx="22" cy="15" r="4.5"/><ellipse cx="22" cy="38" rx="11" ry="3"/></svg></div>
  <h4>Location</h4><p>Venue Address</p>
</div>
<div class="info" style="left:817px;top:2428px">
  <div class="info-icon"><svg width="44" height="44" viewBox="0 0 44 44" fill="none" stroke="#141414" stroke-width="1.8"><path d="M20 14c-6 3-9 10-9 15 0 6 5 9 11 9s11-3 11-9c0-5-3-12-9-15z"/><path d="M18 14l-2-6h12l-2 6"/><text x="22" y="32" font-size="12" text-anchor="middle" fill="#141414" stroke="none" font-family="Outfit,sans-serif">$</text><rect x="5" y="30" width="9" height="9"/></svg></div>
  <h4>Price</h4><p>$230</p>
</div>

<section class="data-protection">
  <div class="center" style="top:2690px;font-size:21px">Data Protection Declaration</div>
  <h2 class="center head" style="top:2721px;font-size:43px">Trust In Every Transaction</h2>

  <div class="contact-band"></div>
  <div class="ring"></div>
  <div class="globe" role="img" aria-label="Illustration of a green globe"></div>

  <div class="node" style="left:573px;top:2850px"><svg width="36" height="36" viewBox="0 0 36 36" fill="none" stroke="#141414" stroke-width="1.6"><ellipse cx="18" cy="8" rx="11" ry="4"/><path d="M7 8v20c0 2 5 4 11 4s11-2 11-4V8M7 15c0 2 5 4 11 4s11-2 11-4M7 22c0 2 5 4 11 4s11-2 11-4"/></svg></div>
  <div class="node" style="left:768px;top:2992px"><svg width="36" height="36" viewBox="0 0 36 36" fill="none" stroke="#141414" stroke-width="1.6"><circle cx="17" cy="19" r="12"/><circle cx="17" cy="19" r="7"/><circle cx="17" cy="19" r="2"/><path d="M17 19L30 6M26 4v6h6"/></svg></div>
  <div class="node" style="left:705px;top:3205px"><svg width="36" height="36" viewBox="0 0 36 36" fill="none" stroke="#141414" stroke-width="1.6"><path d="M18 3l12 5v9c0 8-6 14-12 16C12 31 6 25 6 17V8z"/><rect x="13" y="16" width="10" height="8"/><path d="M15 16v-3a3 3 0 0 1 6 0v3"/></svg></div>
  <div class="node" style="left:447px;top:3207px"><svg width="36" height="36" viewBox="0 0 36 36" fill="none" stroke="#141414" stroke-width="1.6"><path d="M8 4h16l5 5v23H8z"/><path d="M12 12h12M12 17h12M12 22h8"/><circle cx="22" cy="27" r="3"/></svg></div>
  <div class="node" style="left:377px;top:2993px"><svg width="38" height="38" viewBox="0 0 38 38" fill="none" stroke="#141414" stroke-width="1.6"><circle cx="19" cy="8" r="3.5"/><circle cx="7" cy="26" r="3.5"/><circle cx="31" cy="26" r="3.5"/><path d="M13 15h12M19 12v8l-9 3M19 20l9 3M2 35c0-3 2-5 5-5s5 2 5 5M26 35c0-3 2-5 5-5s5 2 5 5"/></svg></div>

  <svg class="abs" style="left:640px;top:2832px" width="60" height="30" viewBox="0 0 60 30" fill="none" stroke="#141414" stroke-width="1.5"><path d="M2 26c10-14 30-20 52-18M46 3l8 5-7 6"/></svg>
  <svg class="abs" style="left:840px;top:3034px" width="30" height="26" viewBox="0 0 30 26" fill="none" stroke="#141414" stroke-width="1.5"><path d="M3 3l22 18M16 22h9v-9"/></svg>
  <svg class="abs" style="left:693px;top:3275px" width="34" height="22" viewBox="0 0 34 22" fill="none" stroke="#141414" stroke-width="1.5"><path d="M30 3C24 12 16 16 5 17M11 11l-6 6 7 3"/></svg>
  <svg class="abs" style="left:392px;top:3222px" width="52" height="28" viewBox="0 0 52 28" fill="none" stroke="#141414" stroke-width="1.5"><path d="M50 24C35 22 18 16 5 6M4 16l1-10 10 1"/></svg>
  <svg class="abs" style="left:375px;top:2958px" width="20" height="34" viewBox="0 0 20 34" fill="none" stroke="#141414" stroke-width="1.5"><path d="M14 32C9 22 7 13 8 3M2 9l6-7 6 6"/></svg>

  <p class="dp" style="left:721px;top:2826px;width:410px"><strong>Data Collection</strong>We Collect Personal Information Like Your Name, Email, Payment Details, And Driving Preferences When You Register Or Interact With Our Website.</p>
  <p class="dp" style="left:89px;top:2869px;width:340px"><strong>Third-Party Sharing</strong>We Do Not Share Your Data Unless Necessary For Providing Services. Any Third-Party Services We Use Follow Strict Data Protection Practices.</p>
  <p class="dp" style="left:834px;top:3066px;width:306px"><strong>Purpose Of Data</strong>Your Data Helps Us Provide Driving Lessons, Communicate With You, And Improve Our Services. We May Also Send Promotional Offers With Your Consent.</p>
  <p class="dp" style="left:61px;top:3145px;width:370px"><strong>Your Rights</strong>You Can Access, Correct, Or Delete Your Data Anytime. Contact Us For Any Requests Or If You Want To Withdraw Consent.</p>
  <p class="dp" style="left:476px;top:3301px;width:270px"><strong>Data Security</strong>We Protect Your Data With Encryption, Access Controls, And Regular Audits To Keep Your Information Safe.</p>
</section>

<section class="contact">
  <div class="center" style="top:3456px;font-size:21px">Contact Us</div>
  <h2 class="center head" style="top:3488px;font-size:43px">Trust In Every Transaction</h2>
  <div class="field" style="left:162px;top:3573px;width:425px;height:44px">Name</div>
  <div class="field" style="left:611px;top:3573px;width:428px;height:44px">Phone</div>
  <div class="field" style="left:162px;top:3642px;width:877px;height:44px">Email Address</div>
  <div class="field" style="left:162px;top:3712px;width:877px;height:124px">Message</div>
  <div class="btn submit">Submit Now</div>
</section>

<footer class="site-footer">
  <div class="foot-brand">Tolesk Drive</div>
  <nav class="foot-nav"><span>Home</span><span>Registration</span><span>Advanced Seminar</span><span>Data Protection</span><span>Imprint</span><span>Contact</span></nav>
  <div class="social" aria-label="Social media links"><span></span><span></span><span></span><span></span></div>
  <div class="foot-rule"></div>
  <div class="foot-copy">Copyright © 2024 All Right Reserved <b>Velora Studio</b></div>
  <div class="foot-links"><span>Privacy Policy</span><span>Terms Of Service</span><span>Cookies Settings</span></div>
</footer>

</body>
</html>
```